Business Card Design For A Renovation Contractor Company

We need a business card for a new company based in Singapore, our company name is "KT Planora". We are a renovation contractor that builds designs into reality. We build more of F&B restaurants, retail stores and commercial offices. We work very closely with designers. The final design should communicate to our client that we are a company that you can trust, that will plan and complete your project without giving you a headache. I like my client to remember my company as "KT". The beauty of SIMPLE is important.

Industry/Entity Type

Contractor

Requirements
Nice to have
• Black or Red base

```html
<!DOCTYPE html>
<html lang="en">
<head>
<meta charset="utf-8">
<title>KT Planora – Business Card</title>
<link rel="stylesheet" href="https://fonts.googleapis.com/css2?family=Tinos:wght@400;700&family=Arimo:wght@400&display=swap">
<style>
  :root {
    --card-bg: #ffffff;
    --ink: #111111;
    --brand-red: #e3141b;
    --rule-grey: #555555;
    --serif: "Tinos", "Times New Roman", serif;
    --sans: "Arimo", Arial, sans-serif;
  }
  html, body {
    margin: 0;
    padding: 0;
    overflow: hidden;
    background: var(--card-bg);
  }
  .card {
    position: relative;
    width: 1200px;
    height: 720px;
    background: var(--card-bg);
    overflow: hidden;
    color: var(--ink);
    font-family: var(--serif);
  }
  .brand {
    position: absolute;
    left: 0;
    top: 108px;
    width: 1200px;
    text-align: center;
  }
  .brand-mark {
    display: block;
    margin: 0 auto;
  }
  .brand-name {
    margin: 4px 0 0;
    font-family: var(--serif);
    font-weight: 400;
    font-size: 62px;
    line-height: 1;
    color: var(--ink);
    letter-spacing: 0.5px;
  }
  .brand-tagline {
    display: inline-block;
    margin-top: 4px;
    padding-top: 3px;
    border-top: 2px solid var(--rule-grey);
    font-family: var(--sans);
    font-size: 22px;
    line-height: 1;
    color: var(--ink);
    letter-spacing: 0.4px;
  }
  .person {
    position: absolute;
    left: 172px;
    top: 522px;
    width: 380px;
  }
  .person-name {
    margin: 0 0 0 5px;
    font-family: var(--serif);
    font-weight: 400;
    font-size: 53px;
    line-height: 1;
    color: var(--brand-red);
    text-shadow: 0 0 6px rgba(227, 20, 27, 0.45);
  }
  .person-title {
    margin: 11px 0 0 5px;
    font-size: 15px;
    line-height: 1;
    letter-spacing: 26px;
    color: var(--ink);
  }
  .person-email {
    margin: 12px 0 0;
    font-size: 34px;
    line-height: 1.1;
    color: var(--ink);
  }
  .divider {
    position: absolute;
    left: 600px;
    top: 526px;
    width: 4px;
    height: 127px;
    background: var(--brand-red);
    box-shadow: 0 0 4px rgba(227, 20, 27, 0.5);
  }
  .address {
    position: absolute;
    left: 684px;
    top: 514px;
    margin: 0;
    font-style: normal;
    font-size: 25px;
    line-height: 51px;
    color: var(--ink);
  }
</style>
</head>
<body>
  <main class="card">
    <header class="brand">
      <svg class="brand-mark" width="112" height="112" viewBox="0 0 112 112" aria-hidden="true">
        <circle cx="56" cy="56" r="48" fill="none" stroke="var(--brand-red)" stroke-width="10"/>
      </svg>
      <h1 class="brand-name">KT Planora</h1>
      <div class="brand-tagline">turning designs into spaces</div>
    </header>

    <section class="person">
      <h2 class="person-name">Marcus Tan.</h2>
      <p class="person-title">DIRECTOR</p>
      <p class="person-email">Marcus@ktplanora.com</p>
    </section>

    <div class="divider"></div>

    <address class="address">
      12 TELOK AYER WAY<br>
      #03-1208 TELOK AYER COURT<br>
      SINGAPORE 068914
    </address>
  </main>
</body>
</html>
```